Software engineering company needs business card

I need a cool business card. Company: Soft Belan Brindlewood Ave 41 58207 Sincity Name: Gerald Vanholt CEO / Managing Director & Owner

```html
<!DOCTYPE html>
<html lang="en">
<head>
<meta charset="utf-8">
<title>Soft Belan – Business Card</title>
<link rel="stylesheet" href="https://fonts.googleapis.com/css2?family=Oswald:wght@500&family=Open+Sans:wght@300;400;600&display=swap">
<style>
  :root {
    --backdrop: #d4d4d4;
    --card: #1f1f20;
    --card-edge: #2a2a2b;
    --white: #f4f4f4;
    --silver: #b9b9bb;
    --muted: #a8a8aa;
    --accent: #7cc242;
    --divider: #4a4a4c;
  }
  * { box-sizing: border-box; margin: 0; padding: 0; }
  html, body {
    width: 1200px; height: 1000px; overflow: hidden;
    background: var(--backdrop);
  }
  .stage {
    position: relative; width: 1200px; height: 1000px;
    display: flex; flex-direction: column; align-items: center; justify-content: center; gap: 70px;
  }
  .card {
    position: relative; width: 560px; height: 320px;
    background: var(--card);
    border-radius: 30px;
    box-shadow: 0 12px 28px rgba(0,0,0,0.28);
    overflow: hidden;
  }
  /* Front */
  .card--front { display: flex; align-items: center; justify-content: center; }
  .brand-name {
    font-family: "Open Sans", sans-serif; font-weight: 300;
    font-size: 54px; letter-spacing: 8px; text-transform: uppercase;
    color: var(--silver);
  }
  /* Back */
  .card--back { font-family: "Open Sans", sans-serif; }
  .identity {
    position: absolute; left: 40px; bottom: 52px;
  }
  .identity__name {
    font-family: "Oswald", sans-serif; font-weight: 500;
    font-size: 30px; letter-spacing: 0.5px; text-transform: uppercase;
    color: var(--white); line-height: 1.1;
  }
  .identity__role {
    font-size: 15px; font-weight: 400; color: var(--accent); margin-top: 2px;
  }
  .divider {
    position: absolute; left: 318px; top: 96px; width: 1px; height: 170px;
    background: var(--divider);
  }
  .contact {
    position: absolute; left: 338px; top: 100px;
    font-size: 13.5px; font-weight: 400; color: var(--muted); line-height: 1.35;
  }
  .contact__address { margin-bottom: 8px; }
  .contact__list { list-style: none; }
  .contact__item { display: flex; align-items: center; gap: 12px; height: 20px; }
  .contact__icon { width: 11px; height: 11px; fill: var(--accent); flex: none; }
  .contact__web .accent { color: var(--accent); }
</style>
</head>
<body>
<main class="stage">
  <section class="card card--front" aria-label="Card front">
    <span class="brand-name">Soft Belan</span>
  </section>

  <section class="card card--back" aria-label="Card back">
    <div class="identity">
      <h1 class="identity__name">Gerald Vanholt</h1>
      <p class="identity__role">CEO / Geschaftsfuhrer &amp; Inhaber</p>
    </div>
    <div class="divider"></div>
    <div class="contact">
      <p class="contact__address">Brindlewood Ave 41<br>58207 Sincity</p>
      <ul class="contact__list">
        <li class="contact__item">
          <svg class="contact__icon" viewBox="0 0 24 24" aria-hidden="true"><path d="M6.6 10.8a15 15 0 0 0 6.6 6.6l2.2-2.2a1 1 0 0 1 1-.25 11.4 11.4 0 0 0 3.6.57 1 1 0 0 1 1 1V20a1 1 0 0 1-1 1A17 17 0 0 1 3 4a1 1 0 0 1 1-1h3.5a1 1 0 0 1 1 1c0 1.25.2 2.45.57 3.57a1 1 0 0 1-.25 1z"/></svg>
          <span>+000 482 719 305</span>
        </li>
        <li class="contact__item">
          <svg class="contact__icon" viewBox="0 0 24 24" aria-hidden="true"><path d="M2 5h20v14H2z M2 5l10 8 10-8" stroke="#1f1f20" stroke-width="1.6"/></svg>
          <span>hello@softbelan.com</span>
        </li>
        <li class="contact__item contact__web">
          <svg class="contact__icon" viewBox="0 0 24 24" aria-hidden="true"><circle cx="12" cy="12" r="10"/><path d="M2 12h20M12 2c3 3 3 17 0 20M12 2c-3 3-3 17 0 20" stroke="#1f1f20" stroke-width="1.5" fill="none"/></svg>
          <span>www.<span class="accent">softbelan</span>.com</span>
        </li>
      </ul>
    </div>
  </section>
</main>
</body>
</html>
```